Vorimelo Mobile App

We are in need of a design for a mobile application that delivers relevant content to users based on the profile that they enter and based on the answers that they enter in a daily health tracker. There also will be functionality that will allow a user to check the cost of a medical service/ procedure before going to the medical provider (could get a list of providers and costs after entering procedure, service or prescription in a search box). The content will be articles or information that our team will find/develop on a daily basis and put into a database that the app will pull off of. The profile needs to capture age, sex, ethinicity (optional) and then have a list of topics that the user can select to get daily updated information/content. These topics are: Diabetes, Heart Disease, Hypertension, COPD, Back Pain, Weight Management, Depression, Cancer, Wellness Plan. The final design should allow for users to receive helpful health care information every day based on their profile and the answers in the daily health tracker.

Medical

```html
<!DOCTYPE html>
<html lang="en">
<head>
<meta charset="utf-8">
<title>Vorimelo Mobile App</title>
<link rel="stylesheet" href="https://fonts.googleapis.com/css2?family=Roboto:wght@300;400;500&display=swap">
<style>
  :root {
    --stage: #2b2b2b;
    --sky: #3cb6e8;
    --sky-dark: #2a9bcb;
    --leaf: #86c451;
    --leaf-dark: #5f9a2f;
    --ink: #3a3a3a;
    --muted: #8d8d8d;
    --line: #d9d9d9;
    --paper: #ffffff;
    --tile: #f1f0ee;
  }
  * { box-sizing: border-box; margin: 0; padding: 0; }
  html, body { width: 1200px; height: 975px; overflow: hidden; }
  body {
    position: relative;
    background: var(--stage);
    font-family: "Roboto", Arial, sans-serif;
    color: var(--ink);
  }

  /* App icon */
  .app-icon {
    position: absolute; left: 123px; top: 146px; width: 255px; height: 255px;
    border-radius: 30px; background: var(--tile);
    border: 2px solid #dcdad6;
    display: flex; align-items: center; justify-content: center;
  }
  .app-icon__name { font-size: 40px; font-weight: 500; color: var(--sky); }

  /* Screens */
  .screen { position: absolute; width: 319px; background: var(--paper); overflow: hidden; }
  .screen--login { left: 398px; top: 146px; height: 567px; }
  .screen--tracker { left: 742px; top: 146px; height: 764px; }

  .status-bar {
    height: 20px; background: var(--sky); color: #fff;
    font-size: 11.5px; display: flex; align-items: center;
    padding: 0 6px; position: relative;
  }
  .status-bar__carrier { display: flex; align-items: center; gap: 4px; }
  .status-bar__time { position: absolute; left: 0; right: 0; text-align: center; }
  .status-bar__power { margin-left: auto; display: flex; align-items: center; gap: 4px; }
  .battery { width: 22px; height: 9px; border: 1px solid #fff; border-radius: 2px; padding: 1px; position: relative; }
  .battery::before { content: ""; display: block; width: 100%; height: 100%; background: #fff; }
  .battery::after { content: ""; position: absolute; right: -3px; top: 2px; width: 2px; height: 3px; background: #fff; }

  .title-bar {
    height: 45px; background: var(--sky); color: #fff;
    display: flex; align-items: center; justify-content: center;
    font-size: 20px; font-weight: 300; position: relative;
  }
  .title-bar__back { position: absolute; left: 7px; top: 11px; }

  /* Login */
  .brand { position: absolute; top: 117px; left: 0; right: 0; text-align: center; }
  .brand__name { font-size: 34px; font-weight: 500; color: var(--sky); line-height: 1; }
  .brand__tagline { margin-top: 6px; font-size: 15px; color: #6d6d6d; }

  .field-label { position: absolute; left: 26px; font-size: 13px; color: #555; }
  .field-input { position: absolute; left: 26px; width: 259px; height: 40px; border: 1px solid #c9c9c9; background: #fff; }

  .btn {
    position: absolute; display: flex; align-items: center; justify-content: center;
    color: #fff; font-size: 16px; font-weight: 400;
  }
  .btn--primary { background: var(--leaf); border-bottom: 3px solid var(--leaf-dark); }
  .btn--secondary { background: var(--sky); border-bottom: 3px solid var(--sky-dark); }
  .login__btn { left: 26px; top: 391px; width: 259px; height: 46px; }
  .login__forgot { position: absolute; top: 466px; left: 0; right: 0; text-align: center; font-size: 13px; color: #666; }

  /* Tracker */
  .question { position: absolute; left: 0; right: 0; padding: 0 13px 0 16px; border-bottom: 1px solid var(--line); }
  .question--open { border-bottom: none; }
  .question__text { font-size: 13.3px; line-height: 17px; color: var(--ink); font-weight: 400; }
  .options { display: flex; align-items: center; gap: 7px; margin-top: 6px; white-space: nowrap; }
  .option { display: flex; align-items: center; gap: 5px; font-size: 11.3px; color: var(--muted); white-space: nowrap; }
  .option.is-checked { color: var(--ink); }
  .option__mark {
    width: 21px; height: 21px; border-radius: 50%;
    border: 1.3px solid #9a9a9a; position: relative; flex: none;
  }
  .option.is-checked .option__mark { border: none; background: var(--leaf); }
  .option.is-checked .option__mark::after {
    content: ""; position: absolute; left: 8px; top: 4px; width: 5px; height: 10px;
    border: solid #fff; border-width: 0 2px 2px 0; transform: rotate(45deg);
  }
  .insulin-entry { display: flex; align-items: center; gap: 6px; margin-top: 12px; font-size: 11.5px; color: var(--muted); }
  .insulin-entry__box { width: 55px; height: 18px; border: 1px solid #b5b5b5; font-size: 12px; color: var(--ink); text-align: right; padding-right: 4px; line-height: 16px; }
  .tracker__submit { left: 30px; top: 548px; width: 259px; height: 46px; }
  .tracker__email { left: 30px; top: 603px; width: 259px; height: 46px; }
</style>
</head>
<body>

  <div class="app-icon"><span class="app-icon__name">Vorimelo</span></div>

  <section class="screen screen--login">
    <div class="status-bar">
      <span class="status-bar__carrier">●●●○○ NOVA
        <svg width="12" height="9" viewBox="0 0 12 9"><path d="M1 3.5a7 7 0 0 1 10 0M3 5.5a4 4 0 0 1 6 0" stroke="#fff" stroke-width="1.3" fill="none"/><circle cx="6" cy="7.6" r="1.2" fill="#fff"/></svg>
      </span>
      <span class="status-bar__time">4:21 PM</span>
      <span class="status-bar__power">ᛒ 100% <span class="battery"></span></span>
    </div>
    <div class="title-bar">Login</div>

    <div class="brand">
      <div class="brand__name">Vorimelo</div>
      <div class="brand__tagline">Health Care Connected</div>
    </div>

    <label class="field-label" style="top:231px">Email</label>
    <div class="field-input" style="top:251px"></div>
    <label class="field-label" style="top:306px">Password</label>
    <div class="field-input" style="top:326px"></div>

    <div class="btn btn--primary login__btn">Login</div>
    <div class="login__forgot">Forgot Your Password?</div>
  </section>

  <section class="screen screen--tracker">
    <div class="status-bar">
      <span class="status-bar__carrier">●●●○○ NOVA
        <svg width="12" height="9" viewBox="0 0 12 9"><path d="M1 3.5a7 7 0 0 1 10 0M3 5.5a4 4 0 0 1 6 0" stroke="#fff" stroke-width="1.3" fill="none"/><circle cx="6" cy="7.6" r="1.2" fill="#fff"/></svg>
      </span>
      <span class="status-bar__time">4:21 PM</span>
      <span class="status-bar__power">ᛒ 100% <span class="battery"></span></span>
    </div>
    <div class="title-bar">
      <svg class="title-bar__back" width="24" height="24" viewBox="0 0 24 24"><circle cx="12" cy="12" r="10.5" stroke="#fff" stroke-width="1.6" fill="none"/><path d="M13.5 7.5 9 12l4.5 4.5" stroke="#fff" stroke-width="1.8" fill="none"/></svg>
      Vorimelo
    </div>

    <div class="question" style="top:77px;height:56px">
      <p class="question__text">How many hours did you sleep last night?</p>
      <div class="options">
        <span class="option"><span class="option__mark"></span>Less than 6 hours</span>
        <span class="option is-checked"><span class="option__mark"></span>More than 6 hours</span>
      </div>
    </div>

    <div class="question" style="top:141px;height:57px">
      <p class="question__text">Have you exercised today?</p>
      <div class="options">
        <span class="option"><span class="option__mark"></span>Yes</span>
        <span class="option is-checked"><span class="option__mark"></span>No</span>
      </div>
    </div>

    <div class="question" style="top:205px;height:57px">
      <p class="question__text">Have you had a cigarette today?</p>
      <div class="options">
        <span class="option"><span class="option__mark"></span>Yes</span>
        <span class="option is-checked"><span class="option__mark"></span>No</span>
      </div>
    </div>

    <div class="question" style="top:266px;height:56px">
      <p class="question__text">Have you had any alcoholic beverages today?</p>
      <div class="options">
        <span class="option"><span class="option__mark"></span>Yes</span>
        <span class="option is-checked"><span class="option__mark"></span>No</span>
      </div>
    </div>

    <div class="question" style="top:330px;height:74px">
      <p class="question__text">How would you describe your eating over the last 24 hours?</p>
      <div class="options">
        <span class="option"><span class="option__mark"></span>Healthy</span>
        <span class="option is-checked"><span class="option__mark"></span>Not bad</span>
        <span class="option is-checked"><span class="option__mark"></span>Needs Improvement</span>
      </div>
    </div>

    <div class="question" style="top:410px;height:75px">
      <p class="question__text">How would you describe your stress level over the last 24 hours?</p>
      <div class="options">
        <span class="option"><span class="option__mark"></span>Low/None</span>
        <span class="option is-checked"><span class="option__mark"></span>Slightly Elevated</span>
        <span class="option is-checked"><span class="option__mark"></span>High</span>
      </div>
    </div>

    <div class="question question--open" style="top:492px">
      <p class="question__text">Have you checked your insulin levels today?</p>
      <div class="insulin-entry">If yes, enter results here: <span class="insulin-entry__box">#</span></div>
    </div>

    <div class="btn btn--primary tracker__submit">Submit to Your Health Tracker</div>
    <div class="btn btn--secondary tracker__email">Email Report</div>

    <div class="question question--open" style="top:667px">
      <p class="question__text">Have you taken all prescribed medicines as instructed in the last 24 hours?</p>
      <div class="options">
        <span class="option"><span class="option__mark"></span>Yes</span>
        <span class="option is-checked"><span class="option__mark"></span>No</span>
      </div>
    </div>
  </section>

</body>
</html>
```